Start Up Incubator requires a cool, chic website matching logo theme, CODING + DESIGN

Please see the attached brief file,

This project is to code and design, please DO NOT waste both your and my time by submitting off the rack copy/paste designs without reading the brief or looking at our logo, brand feel and image.

Thank you

Target Market(s)

Male and Female
18-40 Years of Age
Varying levels of business experience
Creative
Social Networker
Technologically Savvy

Requirements
Must have
• Color and feel as per logo manual

```html
<!DOCTYPE html>
<html lang="en">
<head>
<meta charset="utf-8">
<title>Nova Hatch</title>
<link href="https://fonts.googleapis.com/css2?family=Bodoni+Moda:opsz,wght@6..96,400;6..96,500&family=Raleway:wght@300;400;500;600&display=swap" rel="stylesheet">
<style>
:root{
  --yellow:#f6ae00;
  --dark:#3b3b3b;
  --darker:#2e2e2e;
  --ink:#222;
  --text:#333;
  --grey-bg:#ebebed;
  --line:#cfcfcf;
  --beige:#f2d596;
  --sand:#e9dfc6;
  --mist:#ececee;
  --link:#1a8ccf;
  --fb:#4b5f8c;
  --sky:#2aa3d9;
  --umber:#6b5a52;
  --green:#3fae5b;
}
*{box-sizing:border-box;margin:0;padding:0}
html,body{width:1200px;height:2826px;overflow:hidden;background:#fff}
body{font-family:"Raleway",sans-serif;color:var(--text)}
.page{position:relative;width:1200px;height:2826px;overflow:hidden}
.abs{position:absolute}
.brand,.quote,.h-sec,.tab h3,.tile h4,.feed-head h5,.contact-head h2,.details h3{
  font-family:"Bodoni Moda",serif;font-weight:400;font-variation-settings:"opsz" 96;
}

/* header */
.topbar{left:0;top:0;width:1200px;height:113px;background:var(--yellow)}
.brand{left:0;top:40px;width:1200px;text-align:center;font-size:42px;letter-spacing:6px;color:var(--dark)}
.flags{left:983px;top:68px;display:flex;gap:8px}
.flags svg{display:block}
.mainnav{left:0;top:113px;width:1200px;height:83px;background:linear-gradient(#454545,#2f2f2f)}
.navlist{display:flex;justify-content:center;gap:52px;list-style:none;height:83px;align-items:center;font-size:17px;font-weight:300;color:var(--yellow)}

/* hero */
.hero{left:0;top:196px;width:1200px;height:524px;background:linear-gradient(100deg,#efe9e3 0%,#d9d4cf 35%,#8a8fa0 58%,#3a4466 80%,#2b3353 100%)}
.quote{left:150px;top:310px;width:400px;color:#2e2e2e;text-align:center;line-height:1}
.quote .l{display:block}
.quote .lg{font-size:50px}
.quote .sm{font-size:34px}
.quote .xl{font-size:80px}
.dots{left:300px;top:648px;display:flex;gap:14px}
.dots span{width:16px;height:16px;border-radius:50%;background:#555}

/* welcome */
.welcome{left:0;top:738px;width:1200px;text-align:center}
.h-sec{font-size:30px;color:var(--ink);line-height:1.2}
.sub{font-size:18px;font-weight:300;color:#333;margin-top:2px}
.welcome p{width:870px;margin:12px auto 0;font-size:13px;line-height:20px;color:#333}
.btn-more{left:552px;top:874px;width:94px;height:38px;background:var(--yellow);color:#222;font-size:14px;display:flex;align-items:center;justify-content:center}

/* tabs */
.tabs{left:139px;top:936px;width:922px;height:78px;display:flex;align-items:stretch}
.tab{text-align:center;padding-top:12px}
.tab h3{font-size:23px;color:var(--ink);line-height:30px}
.tab span{font-size:17px;font-weight:300}
.tab.active{background:var(--dark);width:300px}
.tab.active h3,.tab.active span{color:var(--yellow)}
.tab.mid{width:292px;position:relative}
.tab.mid::after{content:"";position:absolute;right:0;top:10px;height:56px;border-right:1px solid #e0c27a}
.tab.last{width:330px}
.tabpanel{left:139px;top:1017px;width:922px;height:104px;background:var(--yellow);padding:14px 26px;color:#fff;font-size:13px;font-weight:600;line-height:20px}

/* gallery */
.gallery-head{left:0;top:1138px;width:1200px;text-align:center}
.grid{left:136px;top:1209px;display:grid;grid-template-columns:repeat(4,222px);grid-auto-rows:172px;gap:15px 13px}
.tile{display:flex;flex-direction:column;align-items:center;justify-content:center}
.tile h4{font-size:20px;color:var(--ink)}
.tile small{font-size:14px;font-weight:300;color:#444}
.t-beige{background:var(--beige)}
.t-sand{background:var(--sand)}
.t-mist{background:var(--mist)}
.ph-office{background:linear-gradient(135deg,#e6e8ec,#9aa0a8 55%,#2f3136)}
.ph-meeting{background:linear-gradient(135deg,#e5b24a,#c99236 60%,#8a6a2c)}
.ph-words{background:linear-gradient(135deg,#f2c94c,#e39a1f 60%,#c77b17)}
.ph-table{background:linear-gradient(135deg,#d9a640,#a07a2e 60%,#5c4a22)}

/* feeds */
.feed-head{display:flex;align-items:center;gap:16px}
.feed-head .dot{width:45px;height:45px;border-radius:50%}
.feed-head h5{font-size:23px;color:var(--ink)}
.social-col{left:147px;top:1604px}
.news-col{left:433px;top:1604px}
.photo-col{left:727px;top:1604px}
.social-text{left:207px;top:1680px;width:220px;font-size:12.5px;font-weight:600;line-height:19px;color:#222}
.avatars{left:170px;top:1737px;display:flex;gap:9px}
.avatars span{width:53px;height:53px;background:linear-gradient(#d8c2ac,#8f7563)}
.btn-join{left:171px;top:1805px;width:95px;height:28px;background:var(--fb);color:#fff;font-size:11px;font-weight:500;display:flex;align-items:center;justify-content:center;border-radius:2px}
.post{left:448px;width:240px;font-size:12.5px;line-height:18px;color:#222;font-weight:500}
.post b{color:var(--link);font-weight:600}
.post a{color:var(--link);text-decoration:none}
.post time{display:block;color:#777;font-weight:400;margin-top:3px}
.photocard{left:735px;top:1667px;width:282px;height:174px;background:#fff;box-shadow:0 1px 4px rgba(0,0,0,.3);padding:8px}
.photocard-img{width:266px;height:123px;background:linear-gradient(135deg,#cfe0ea,#7f9db0 55%,#37515f)}
.photocard-foot{display:flex;justify-content:space-between;align-items:center;margin-top:6px;font-size:11px;font-weight:600;color:var(--fb)}
.photocard-foot svg{vertical-align:middle;margin-right:6px}
.btn-comment{background:var(--green);color:#fff;padding:5px 14px;font-size:11px}

/* contact */
.contact{left:0;top:1871px;width:1200px;height:767px;background:var(--grey-bg)}
.contact-head{left:0;top:1918px;width:1200px;text-align:center}
.contact-head h2{font-size:23px;color:var(--ink);letter-spacing:1px}
.contact-head p{font-size:17px;font-weight:300;margin-top:14px;color:#333}
.form{left:177px;top:2020px;width:558px;height:520px;background:var(--dark)}
.field{height:60px;border-bottom:1px solid var(--line);color:#fff;font-size:16px;padding:18px 19px}
.field.msg{border:none;height:auto}
.btn-submit{left:603px;top:2540px;width:132px;height:52px;background:var(--yellow);color:#222;font-size:17px;display:flex;align-items:center;justify-content:center}
.details{left:771px;top:2018px;font-size:13.5px;line-height:22px;color:#333}
.details h3{font-size:21px;color:var(--ink);margin-bottom:16px}
.details p{margin-bottom:18px}

/* footer */
.footer{left:0;top:2638px;width:1200px;height:132px;background:linear-gradient(#474747,#2d2d2d)}
.footnav{display:flex;gap:43px;list-style:none;padding:26px 0 0 143px;font-size:14px;font-weight:300;color:var(--yellow)}
.socials{display:flex;gap:12px;position:absolute;left:499px;top:66px}
.socials span{width:29px;height:29px;background:#555}
.socials span.on{background:var(--yellow)}
.copybar{left:0;top:2770px;width:1200px;height:56px;background:var(--yellow);text-align:center;font-size:13px;line-height:56px;color:#333}
</style>
</head>
<body>
<div class="page">

  <header>
    <div class="abs topbar"></div>
    <div class="abs brand">NOVA HATCH</div>
    <div class="abs flags" aria-label="Language choice">
      <svg width="32" height="22" viewBox="0 0 32 22" role="img" aria-label="English">
        <rect width="32" height="22" fill="#2b3f8c"/>
        <rect x="13" width="6" height="22" fill="#fff"/><rect y="8" width="32" height="6" fill="#fff"/>
        <rect x="14.5" width="3" height="22" fill="#c8202f"/><rect y="9.5" width="32" height="3" fill="#c8202f"/>
      </svg>
      <svg width="32" height="22" viewBox="0 0 32 22" role="img" aria-label="Deutsch">
        <rect width="32" height="7.4" fill="#111"/><rect y="7.3" width="32" height="7.4" fill="#d4141c"/><rect y="14.6" width="32" height="7.4" fill="#f5c400"/>
      </svg>
    </div>
    <nav class="abs mainnav">
      <ul class="navlist">
        <li>Home</li><li>About Us</li><li>Product Offering</li><li>Case Studies</li><li>Download</li><li>Media Gallery</li><li>Contact Us</li>
      </ul>
    </nav>
  </header>

  <section>
    <div class="abs hero" role="img" aria-label="Photo of two smiling businessmen in suits looking at a laptop in a bright office"></div>
    <blockquote class="abs quote">
      <span class="l"><span class="lg">“ G</span><span class="sm">REAT </span><span class="lg">I</span><span class="sm">DEAS</span></span>
      <span class="l" style="margin-top:10px"><span class="sm">NEED </span><span class="lg">L</span><span class="sm">ANDING</span></span>
      <span class="l" style="margin-top:10px"><span class="lg">G</span><span class="sm">EAR AS WELL AS</span></span>
      <span class="l" style="margin-top:14px"><span class="xl">WINGS</span><span class="lg"> ”</span></span>
    </blockquote>
    <div class="abs dots"><span></span><span></span><span></span><span></span></div>
  </section>

  <section class="abs welcome">
    <h2 class="h-sec">WELCOME</h2>
    <div class="sub">Home Content</div>
    <p>Nemo enim ipsam voluptatem quia voluptas sit aspernatur aut odit aut fugit, sed quia consequuntur magni dolores eos qui ratione voluptatem sequi nesciunt. Neque porro quisquam est, qui dolorem ipsum quia dolor sit amet, consectetur, adipisci velit, sed quia non numquam eius modi tempora incidunt</p>
  </section>
  <div class="abs btn-more">Read more</div>

  <section>
    <div class="abs tabs">
      <div class="tab active"><h3>CASE STUDIES</h3><span>Lorium ipsum Content</span></div>
      <div class="tab mid"><h3>DOWNLOAD</h3><span>Lorium ipsum Content</span></div>
      <div class="tab last"><h3>PRODUCT OFFERING</h3><span>Lorium ipsum Content</span></div>
    </div>
    <div class="abs tabpanel">Nemo enim ipsam voluptatem quia voluptas sit aspernatur aut odit aut fugit, sed quia consequuntur magni dolores eos qui ratione voluptatem sequi nesciunt. Neque porro quisquam est, qui dolorem ipsum quia dolor sit amet, consectetur, adipisci velit, sed quia non numquam eius modi tempora incidunt</div>
  </section>

  <section>
    <div class="abs gallery-head">
      <h2 class="h-sec" style="font-size:24px">MEDIA GALLERY</h2>
      <div class="sub">Lorium ipsum Content</div>
    </div>
    <div class="abs grid">
      <div class="ph-office" role="img" aria-label="Photo of business people walking through a glass office"></div>
      <div class="tile t-beige"><h4>LORIUM IPSUM</h4><small>Lorium ipsum</small></div>
      <div class="ph-meeting" role="img" aria-label="Photo of colleagues at a meeting table, yellow tint"></div>
      <div class="tile t-sand"><h4>LORIUM IPSUM</h4><small>Lorium ipsum</small></div>
      <div class="tile t-beige"><h4>LORIUM IPSUM</h4><small>Lorium ipsum</small></div>
      <div class="ph-words" role="img" aria-label="Word cloud illustration about consulting and services"></div>
      <div class="tile t-mist"><h4>LORIUM IPSUM</h4><small>Lorium ipsum</small></div>
      <div class="ph-table" role="img" aria-label="Photo of a business team around a conference table, yellow tint"></div>
    </div>
  </section>

  <section>
    <div class="abs social-col feed-head"><span class="dot" style="background:var(--fb)"></span><h5>SOCIAL FEED</h5></div>
    <p class="abs social-text">Sed ut perspiciatis unde omnis iste natus error sit voluptatem .</p>
    <div class="abs avatars" role="img" aria-label="Profile photos of four members"><span></span><span></span><span></span><span></span></div>
    <div class="abs btn-join">JOIN TO US</div>

    <div class="abs news-col feed-head"><span class="dot" style="background:var(--sky)"></span><h5>NEWS FEED</h5></div>
    <p class="abs post" style="top:1680px"><b>brightpost</b> Check out Day 321 - Tweet tweet - <a>http://dailyframe.net/day/321/</a><time>12 minutes ago</time></p>
    <p class="abs post" style="top:1762px"><b>brightpost</b> Check out Day 321 - Tweet tweet - <a>http://dailyframe.net/day/321/</a><time>12 minutes ago</time></p>

    <div class="abs photo-col feed-head"><span class="dot" style="background:var(--umber)"></span><h5>PHOTO FEED</h5></div>
    <div class="abs photocard">
      <div class="photocard-img" role="img" aria-label="Photo of an airliner parked at an airport gate"></div>
      <div class="photocard-foot">
        <span><svg width="14" height="12" viewBox="0 0 14 12"><path d="M7 12 1 6a3.3 3.3 0 0 1 6-4 3.3 3.3 0 0 1 6 4z" fill="#3f6fa8"/></svg>23 likes</span>
        <span class="btn-comment">Comment</span>
      </div>
    </div>
  </section>

  <section>
    <div class="abs contact"></div>
    <div class="abs contact-head">
      <h2>GET IN TOUCH</h2>
      <p>We’re currently accepting new client projects. Think we might help? We’d love to hear from you.</p>
    </div>
    <div class="abs form">
      <div class="field">Full Name</div>
      <div class="field">Email Address</div>
      <div class="field">Telephone Number</div>
      <div class="field msg">Message</div>
    </div>
    <div class="abs btn-submit">Submit</div>
    <div class="abs details">
      <h3>CONTACT DETAILS</h3>
      <p>hello@lanternworks.example</p>
      <p>(555) 204-1187</p>
      <p>Lanternworks<br>812 Maple Court, Suite 4<br>Fairview, CA 90210</p>
    </div>
  </section>

  <footer>
    <div class="abs footer">
      <ul class="footnav">
        <li>Home</li><li>About Us</li><li>Product Offering</li><li>Case Studies</li><li>Download</li><li>Media Gallery</li><li>Contact Us</li>
      </ul>
      <div class="socials"><span></span><span></span><span></span><span></span><span class="on"></span></div>
    </div>
    <div class="abs copybar">©2014 WWW.COMPANYNAME.COM</div>
  </footer>

</div>
</body>
</html>
```